Harborline Energy - needs a business card

Harborline Energy is a U.S. based diesel sourcing and distribution company that supports American oil & gas fields through providing quality product and consistent services.

Target Market(s)

Oil and Gas

Contact Information for Business Card

The background of the card must be white to ensure the logo pops.

Font styles to use
Serif
Sans Serif

Colors

Designer to choose colors to be used in the design.

Requirements
Must have
• Front of Card: Tag line: Harborline Energy, Powering America's Oil & Gas fields.
• Not sure if you guys do this part but just in case...
• Dale Menschow
• Owner/CEO
• C:555.318.4076
• E:Dmenschow@harborlineenergy.example
• W:Harborlineenergy.example
• Locations: Servicing the Powder River, DJ basin and Bakken formations.
• Back of Card: " Frac fueling is what we do. We understand how important diesel fuel is to your operation, which is why our main service line is Frac fueling. We assure our supply and stand by our service"

```html
<!DOCTYPE html>
<html lang="en">
<head>
<meta charset="utf-8">
<title>Harborline Energy – Business Card</title>
<link rel="stylesheet" href="https://fonts.googleapis.com/css2?family=Roboto:wght@400;500;700&family=Roboto+Condensed:wght@300;400&display=swap">
<style>
  :root {
    --navy: #002a5c;
    --red: #b30d14;
    --white: #ffffff;
    --paper: #ffffff;
    --backdrop: #ececec;
    --body-grey: #6b6b6b;
  }
  * { box-sizing: border-box; margin: 0; padding: 0; }
  html, body { width: 1125px; height: 1200px; overflow: hidden; }
  body {
    background: var(--backdrop);
    font-family: "Roboto", Arial, sans-serif;
    position: relative;
  }
  .card {
    position: absolute;
    left: 171px;
    width: 826px;
    height: 470px;
    box-shadow: 0 4px 14px rgba(0,0,0,0.18);
  }
  .card--front { top: 106px; background: var(--navy); color: var(--white); }
  .card--back { top: 639px; background: var(--paper); }

  .contact { position: absolute; left: 45px; top: 214px; }
  .contact__name { font-size: 30px; font-weight: 700; line-height: 1.1; }
  .contact__title { font-size: 18px; font-weight: 500; margin-top: 3px; }
  .contact__area { font-size: 19px; line-height: 25px; margin-top: 32px; }
  .contact__list { list-style: none; margin-top: 16px; font-size: 19px; }
  .contact__list li { display: flex; align-items: center; height: 25px; }
  .contact__list svg { width: 18px; height: 18px; margin-right: 12px; fill: var(--white); }

  .front-name {
    position: absolute; right: 40px; top: 80px; width: 360px;
    text-align: center;
  }
  .front-name__dot {
    width: 150px; height: 150px; border-radius: 50%;
    background: var(--red); margin: 0 auto 26px;
  }
  .front-name__text { font-size: 44px; font-weight: 700; line-height: 1.1; color: var(--white); }

  .brand { position: absolute; top: 72px; left: 0; width: 100%; text-align: center; }
  .brand__dot { width: 140px; height: 140px; border-radius: 50%; background: var(--navy); margin: 0 auto 24px; }
  .brand__name { font-size: 38px; font-weight: 700; color: var(--navy); }

  .tagline {
    position: absolute; top: 355px; left: 0; width: 100%;
    display: flex; align-items: center; justify-content: center;
    font-size: 22px; font-weight: 500; color: var(--navy);
  }
  .tagline::before, .tagline::after {
    content: ""; width: 74px; height: 2px; background: var(--red); margin: 0 4px;
  }
  .about {
    position: absolute; top: 392px; left: 50px; right: 50px;
    font-family: "Roboto Condensed", Arial, sans-serif; font-weight: 300;
    font-size: 18px; line-height: 23px; color: var(--body-grey); text-align: center;
  }
</style>
</head>
<body>
  <section class="card card--front">
    <div class="contact">
      <h1 class="contact__name">Dale Menschow</h1>
      <p class="contact__title">Owner/CEO</p>
      <p class="contact__area">Servicing the Powder River<br>DJ basin &amp; Bakken formations.</p>
      <ul class="contact__list">
        <li><svg viewBox="0 0 18 18" aria-hidden="true"><path d="M5 0h8a1.5 1.5 0 0 1 1.5 1.5v15A1.5 1.5 0 0 1 13 18H5a1.5 1.5 0 0 1-1.5-1.5v-15A1.5 1.5 0 0 1 5 0zm0 2v12h8V2zm4 13a1 1 0 1 0 0 2 1 1 0 0 0 0-2z"/></svg>555.318.4076</li>
        <li><svg viewBox="0 0 18 18" aria-hidden="true"><path d="M1 4h16v1L9 10 1 5zM1 7l8 5 8-5v7H1z"/></svg>Dmenschow@harborlineenergy.example</li>
        <li><svg viewBox="0 0 18 18" aria-hidden="true"><circle cx="9" cy="9" r="8"/><path d="M4 6c2 0 3 1 3 3s2 2 2 4M12 3c0 2 2 3 4 3" stroke="#002a5c" stroke-width="1.6" fill="none"/></svg>www.Harborlineenergy.example</li>
      </ul>
    </div>
    <div class="front-name">
      <div class="front-name__dot"></div>
      <p class="front-name__text">Harborline Energy</p>
    </div>
  </section>

  <section class="card card--back">
    <div class="brand">
      <div class="brand__dot"></div>
      <p class="brand__name">Harborline Energy</p>
    </div>
    <h2 class="tagline">Harborline Energy, Powering America’s Oil &amp; Gas fields.</h2>
    <p class="about">Frac fueling is what we do. We understand how important diesel fuel is to your operation, which is why our main service line is Frac fueling. We assure our supply and stand by our service</p>
  </section>
</body>
</html>
```